Kestrel Signs Facebook Banner Design

Design a facebook banner for a sign company. I would like to have a modern approach to it.

Product Offering:
Signs
Banners
Decals
Commercial Wraps

```html
<!DOCTYPE html>
<html lang="en">
<head>
<meta charset="utf-8">
<title>Kestrel Signs – Facebook Banner</title>
<link href="https://fonts.googleapis.com/css2?family=Montserrat:wght@500;600;700;800&display=swap" rel="stylesheet">
<style>
  :root {
    --stage: #b3b5b4;
    --red: #e8313a;
    --ink: #2f2f31;
    --white: #ffffff;
    --paper: #f4f4f4;
    --slate: #5f5f61;
    --slate-dark: #48484a;
  }
  * { margin: 0; padding: 0; box-sizing: border-box; }
  html, body {
    width: 1200px; height: 673px; overflow: hidden;
    background: var(--stage);
    font-family: "Montserrat", Arial, sans-serif;
  }
  .banner {
    position: absolute; left: 20px; top: 121px;
    width: 1160px; height: 430px; overflow: hidden;
    background: linear-gradient(180deg, #f7f7f7 0%, #fbfbfb 60%, #eeeeee 100%);
  }
  .backdrop { position: absolute; inset: 0; }
  .brand {
    position: absolute; left: 123px; top: 30px;
    color: var(--ink); font-weight: 800; line-height: 1;
    text-transform: uppercase;
  }
  .brand-name { display: block; font-size: 50px; letter-spacing: 1px; }
  .brand-sub { display: block; font-size: 40px; letter-spacing: 2px; margin: 4px 0 0 88px; }
  .offer-band {
    position: absolute; left: 0; top: 135px; width: 610px; height: 185px;
    background: var(--red);
  }
  .offer-title {
    position: absolute; left: 56px; top: 181px;
    color: var(--white); font-size: 31px; font-weight: 800; letter-spacing: .5px;
  }
  .offer-list {
    position: absolute; left: 56px; top: 225px;
    color: var(--ink); font-size: 26px; font-weight: 600; line-height: 32px;
    letter-spacing: .3px;
  }
  .contact {
    position: absolute; top: 341px; height: 28px;
    display: flex; align-items: center; gap: 12px;
    color: var(--ink); font-size: 16px; font-weight: 500;
  }
  .contact-phone { left: 47px; }
  .contact-web { left: 266px; gap: 26px; }
  .contact-icon { width: 28px; height: 28px; flex: none; }
  .showcase { position: absolute; inset: 0; }
</style>
</head>
<body>
  <div class="banner">
    <svg class="backdrop" width="1160" height="430" viewBox="0 0 1160 430">
      <defs>
        <linearGradient id="fleetTone" x1="0" y1="0" x2="1" y2="1">
          <stop offset="0" stop-color="#6a6a6c"/>
          <stop offset=".55" stop-color="#5a5a5c"/>
          <stop offset="1" stop-color="#444446"/>
        </linearGradient>
      </defs>
      <path role="img" aria-label="Dimmed photo of wrapped service vans parked on a street"
            d="M558 0 H1160 V151 L982 430 H478 L544 321 C535 230 515 130 524 53 C528 25 540 8 558 0 Z"
            fill="url(#fleetTone)"/>
    </svg>

    <div class="brand">
      <span class="brand-name">Kestrel</span>
      <span class="brand-sub">Signs</span>
    </div>

    <div class="offer-band"></div>
    <h1 class="offer-title">PRODUCT OFFERING:</h1>
    <p class="offer-list">SIGNS | BANNERS | DECALS<br>COMMERCIAL WRAPS</p>

    <div class="contact contact-phone">
      <svg class="contact-icon" viewBox="0 0 28 28">
        <circle cx="14" cy="14" r="14" fill="var(--red)"/>
        <path d="M7 11c0-2 3-3 7-3s7 1 7 3v1.5h-3.2V11c-1-.6-2.3-.8-3.8-.8s-2.8.2-3.8.8v1.5H7z" fill="#fff"/>
        <path d="M9 13h10l1.5 6.5h-13z" fill="#fff"/>
        <circle cx="14" cy="16.3" r="1.8" fill="var(--red)"/>
      </svg>
      <span>+000 000 0000 00</span>
    </div>

    <div class="contact contact-web">
      <svg class="contact-icon" viewBox="0 0 28 28">
        <circle cx="14" cy="14" r="14" fill="var(--red)"/>
        <g fill="none" stroke="#fff" stroke-width="1.4">
          <circle cx="14" cy="14" r="7.5"/>
          <ellipse cx="14" cy="14" rx="3.2" ry="7.5"/>
          <path d="M6.5 14h15M8 10h12M8 18h12"/>
        </g>
      </svg>
      <span>www.kestrelsigns.com</span>
    </div>

    <svg class="showcase" width="1160" height="430" viewBox="0 0 1160 430">
      <defs>
        <linearGradient id="rollupTone" x1="0" y1="0" x2="1" y2="1">
          <stop offset="0" stop-color="#3aa64a"/>
          <stop offset=".45" stop-color="#1f2c3c"/>
          <stop offset="1" stop-color="#2f6fb8"/>
        </linearGradient>
        <radialGradient id="stopTone" cx=".5" cy=".45" r=".6">
          <stop offset="0" stop-color="#c8202a"/>
          <stop offset=".55" stop-color="#b23a38"/>
          <stop offset="1" stop-color="#9a948c"/>
        </radialGradient>
        <linearGradient id="vanTone" x1="0" y1="0" x2="1" y2="1">
          <stop offset="0" stop-color="#f2f3f5"/>
          <stop offset=".55" stop-color="#ec7a2a"/>
          <stop offset="1" stop-color="#5c5e62"/>
        </linearGradient>
      </defs>
      <circle cx="595" cy="230" r="112" fill="var(--white)"/>
      <circle role="img" aria-label="Photo of a row of printed roll-up banner stands" cx="595" cy="230" r="103" fill="url(#rollupTone)"/>
      <circle cx="814" cy="232" r="112" fill="var(--white)"/>
      <circle role="img" aria-label="Photo of a red stop sign on a street pole" cx="814" cy="232" r="103" fill="url(#stopTone)"/>
      <circle cx="1030" cy="229" r="112" fill="var(--white)"/>
      <circle role="img" aria-label="Photo of orange and white commercially wrapped vans" cx="1030" cy="229" r="103" fill="url(#vanTone)"/>
    </svg>
  </div>
</body>
</html>
```